Brisk Tide needs a web page for E-commerce site

Small startup business looking for a custom website for my New Saltwater apparel Co.

COMPANY OVERVIEW

Brisk Tide was founded In Mont Belvieu, Tx, right on the heart of pelham cove.

Brisk Tide is the adrenaline, sweat pumping moment you find yourself setting the hook on a monster fish. This is the moment when all your senses come to life as you work to land that trophy, and after a grueling fight when your hi-fiving your fishing buddies...It's that moment... when the waters and the air around you are Brisk Sweet....All or Nothing...pure Addiction......This is BRISK TIDE

Looking for a sharp clean sexy web page for my ecommerce page

I like the look of black background websites.

www.brisktide-demo.com
Updates

I am using shopvane as my host site if that means anything to y'all

Thank you all for the submissions! There were some great ones!  I will have more projects in the future. thanks again

Target Market(s)

inshore/offshore fishing, saltwater enthusiast

Industry/Entity Type

Business

Requirements
Must have
• logo's

inshore/offshore fishing appeal

compatible with shopvane site

```html
<!DOCTYPE html>
<html lang="en">
<head>
<meta charset="utf-8">
<title>Brisk Tide — Products</title>
<link rel="stylesheet" href="https://fonts.googleapis.com/css2?family=Gochi+Hand&family=Roboto+Condensed:wght@400;700&display=swap">
<style>
  :root {
    --bg: #000;
    --orange: #f39a12;
    --panel-border: #c9c9c9;
    --nav-dark: #1c1c1c;
    --nav-mid: #3a3a3a;
    --white: #fff;
    --tile: #333;
    --tile-text: #f2f2f2;
    --footer: #000;
    --ink: #111;
  }
  * { box-sizing: border-box; margin: 0; padding: 0; }
  html, body { width: 1200px; height: 700px; overflow: hidden; background: var(--bg); }
  .page { position: relative; width: 1200px; height: 700px; overflow: hidden; background: var(--bg); }

  .backdrop {
    position: absolute; inset: 0;
    background:
      radial-gradient(ellipse 140px 220px at 150px 390px, rgba(243,154,18,.28), transparent 70%),
      radial-gradient(ellipse 170px 240px at 1080px 380px, rgba(160,160,160,.22), transparent 70%),
      radial-gradient(ellipse 130px 90px at 1090px 470px, rgba(243,154,18,.22), transparent 70%),
      var(--bg);
  }

  .brand {
    position: absolute; left: 196px; top: 16px;
    font-family: "Gochi Hand", cursive; font-size: 62px; line-height: 1;
    color: var(--orange); letter-spacing: 1px; white-space: nowrap;
  }
  .call {
    position: absolute; left: 755px; top: 32px; width: 190px; text-align: center;
    font-family: "Gochi Hand", cursive; color: var(--orange); line-height: 1;
    white-space: nowrap;
  }
  .call-label { font-size: 24px; }
  .call-number { font-size: 26px; margin-top: 6px; letter-spacing: 1px; }

  .shell {
    position: absolute; left: 201px; top: 94px; width: 779px; height: 480px;
    border: 4px solid var(--panel-border); border-radius: 18px;
    background: var(--white); overflow: hidden;
  }
  .nav {
    position: absolute; left: 0; top: 0; width: 100%; height: 40px;
    background: radial-gradient(ellipse at 20% 50%, var(--nav-mid), var(--nav-dark) 70%);
    border-bottom: 7px solid var(--orange);
    box-shadow: 0 4px 6px rgba(0,0,0,.25);
  }
  .nav-link {
    position: absolute; top: 7px;
    font-family: "Roboto Condensed", sans-serif; font-weight: 700; font-size: 20px;
    color: var(--white); text-decoration: none; white-space: nowrap;
  }
  .search {
    position: absolute; left: 543px; top: 4px; width: 192px; height: 28px;
    border-radius: 14px; background: var(--white);
    font-family: "Roboto Condensed", sans-serif; font-style: italic; font-size: 19px;
    color: #999; padding: 2px 0 0 16px;
  }
  .search svg { position: absolute; right: 12px; top: 3px; }

  .sidebar { position: absolute; left: 17px; top: 66px; width: 164px; }
  .sidebar-title {
    height: 33px; width: 138px; background: var(--white);
    border: 1px solid #ccc; border-bottom: none;
    box-shadow: 0 -2px 3px rgba(0,0,0,.2);
    font-family: "Roboto Condensed", sans-serif; font-weight: 700; font-size: 20px;
    text-align: center; line-height: 32px; color: var(--ink);
  }
  .category {
    display: block; width: 163px; height: 65px; margin-bottom: 9px;
    background: var(--tile); box-shadow: 3px 4px 5px rgba(0,0,0,.45);
    font-family: "Roboto Condensed", sans-serif; font-size: 19px;
    color: var(--tile-text); text-align: center; padding-top: 4px; text-decoration: none;
  }

  .product-shot {
    position: absolute; left: 307px; top: 59px; width: 361px; height: 335px;
    background: linear-gradient(180deg, #ececea 0%, #e2e1dd 55%, #3a2f1f 56%, #2a2418 70%, #1a1a1e 84%, #e4e3df 85%, #e8e7e3 100%);
  }

  .footer {
    position: absolute; left: 0; top: 406px; width: 100%; height: 70px; background: var(--footer);
  }
  .copyright {
    position: absolute; left: 0; width: 750px; top: 25px; text-align: center;
    font-family: "Roboto Condensed", sans-serif; font-weight: 700; font-size: 12px; color: var(--white);
  }
  .social { position: absolute; top: 0; display: flex; gap: 11px; left: 551px; }
  .social-tile {
    width: 43px; height: 44px; border-radius: 8px;
    background: linear-gradient(180deg, #6a6a6a, #3c3c3c);
    box-shadow: 0 1px 2px rgba(255,255,255,.2);
  }

  .reflection {
    position: absolute; left: 201px; top: 580px; width: 779px; height: 120px;
    background: linear-gradient(180deg, #000 0%, #0d0202 55%, #2a1c1a 56%, #3e302e 100%);
  }
</style>
</head>
<body>
<div class="page">
  <div class="backdrop" role="img" aria-label="Background art: sweeping orange and grey swooshes on black"></div>

  <div class="brand">BRISK TIDE</div>

  <div class="call">
    <div class="call-label">CALL US AT</div>
    <div class="call-number">1555 010 2040</div>
  </div>

  <div class="shell">
    <nav class="nav">
      <a class="nav-link" style="left:126px">Home</a>
      <a class="nav-link" style="left:199px">About Us</a>
      <a class="nav-link" style="left:299px">Our Products</a>
      <a class="nav-link" style="left:428px">Contact Us</a>
      <div class="search">Search
        <svg width="36" height="22" viewBox="0 0 36 22" aria-hidden="true">
          <circle cx="22" cy="10" r="8" fill="none" stroke="#888" stroke-width="3"/>
          <line x1="15" y1="15" x2="3" y2="21" stroke="#888" stroke-width="4" stroke-linecap="round"/>
        </svg>
      </div>
    </nav>

    <aside class="sidebar">
      <div class="sidebar-title">Products</div>
      <a class="category">T-Shirts</a>
      <a class="category">Hats</a>
      <a class="category">Shorts</a>
      <a class="category">Hoodies</a>
    </aside>

    <div class="product-shot" role="img" aria-label="Product photo: back and front of a dark brown brand T-shirt above a dark banner"></div>

    <footer class="footer">
      <div class="copyright">Copyright 2013 Your Company USA</div>
      <div class="social">
        <div class="social-tile"></div>
        <div class="social-tile"></div>
        <div class="social-tile"></div>
        <div class="social-tile"></div>
      </div>
    </footer>
  </div>

  <div class="reflection"></div>
</div>
</body>
</html>
```